The K7 Momentum Collective Website

We have a pitch deck and messaging drafted. Target audience is academic institutions and VC investors that have seed money in start ups.

Need a basic website

Industry/Entity Type

LIfe Science, Diagnostic, medical device.

Coding

Coded - Design and coding required

Number of Pages Required

5+ page

```html
<!DOCTYPE html>
<html lang="en">
<head>
<meta charset="utf-8">
<title>The K7 Momentum Collective</title>
<link rel="stylesheet" href="https://fonts.googleapis.com/css2?family=Nunito:wght@400;600;700;800;900&family=Nunito+Sans:wght@400;600;700&display=swap">
<style>
:root{
  --teal:#4bb4c8;
  --teal-dark:#3b97ad;
  --teal-deep:#357f95;
  --teal-head:#3aa6c0;
  --aqua:#cdeff3;
  --aqua-soft:#e4f7f9;
  --ink:#2f3438;
  --muted:#5d6468;
  --line:#d9dfe2;
  --white:#ffffff;
}
*{box-sizing:border-box;margin:0;padding:0}
html,body{width:1200px;height:4585px;overflow:hidden;background:var(--white)}
body{font-family:"Nunito Sans",Arial,sans-serif;color:var(--ink);position:relative}
.page{position:relative;width:1200px;height:4585px;overflow:hidden}
.abs{position:absolute}

/* nav + hero */
.hero{left:0;top:0;width:1200px;height:740px;background:var(--teal)}
.nav{position:absolute;left:0;top:0;width:1200px;height:100px;border-bottom:1px solid rgba(255,255,255,.55);display:flex;justify-content:center;align-items:center;gap:38px}
.nav a{color:var(--white);text-decoration:none;font-size:15px;font-weight:600;font-family:"Nunito",sans-serif}
.hero-title{position:absolute;left:100px;top:185px;color:var(--white);font-family:"Nunito",sans-serif;font-weight:900;font-size:66px;line-height:64px;letter-spacing:.5px}
.hero-tag{position:absolute;left:100px;top:392px;color:var(--white);font-size:20px}
.btn-contact{position:absolute;left:100px;top:447px;width:167px;height:44px;background:var(--teal-deep);color:var(--white);font-size:14px;font-weight:600;display:flex;align-items:center;padding-left:22px}
.btn-contact svg{position:absolute;right:14px;top:11px}
.hero-art{position:absolute;left:500px;top:140px;width:600px;height:470px;border-radius:18px;background:radial-gradient(circle at 50% 45%,#8fd6e3 0%,#6cc6d7 45%,var(--teal) 75%)}
.hero-wave{position:absolute;left:0;top:560px}

/* section headings */
.h2{font-family:"Nunito",sans-serif;font-weight:700;color:var(--teal-head);font-size:36px}
.h2.center{text-align:center;width:1200px;left:0}
.rule{height:3px;width:56px;background:var(--teal-head)}

/* intro */
.intro-art{left:100px;top:910px;width:452px;height:336px;border:4px solid var(--teal);border-radius:26px;background:linear-gradient(135deg,#f4f4f4 0%,#dcdcdc 45%,#e63232 46%,#d01f1f 70%,#e9e9e9 71%,#f7f7f7 100%)}
.intro-text{left:638px;top:880px;width:420px;font-size:14px;line-height:20px;color:var(--ink)}
.intro-text p{margin-top:16px}
.intro-text em{font-style:normal;color:var(--teal-head)}

/* problem/solution */
.band{left:0;top:1360px}
.problem{left:100px;top:1445px;width:515px;font-size:14px;line-height:20px}
.problem p{margin-top:14px}
.problem .lead{font-weight:700;margin-top:16px}
.ticks{list-style:none}
.ticks li{position:relative;padding-left:22px}
.ticks li::before{content:"";position:absolute;left:0;top:3px;width:14px;height:14px;border-radius:50%;background:var(--teal-head)}
.ticks li::after{content:"";position:absolute;left:4px;top:6px;width:5px;height:3px;border-left:2px solid #fff;border-bottom:2px solid #fff;transform:rotate(-45deg)}
.problem-art{left:640px;top:1550px;width:420px;height:380px;border-radius:20px;background:linear-gradient(160deg,#f6d36b 0%,#6fc2e0 30%,#3f7fd0 70%,#2d5fb0 100%);opacity:.9}

/* team */
.team{left:100px;top:2320px;width:1000px;display:flex;gap:14px}
.card{position:relative;width:324px;height:455px;background:var(--white);border-radius:14px;box-shadow:0 4px 22px rgba(40,80,95,.14);text-align:center;padding:80px 22px 0}
.avatar{position:absolute;left:100px;top:-78px;width:124px;height:124px;border-radius:50%;border:5px solid #fff;box-shadow:0 3px 12px rgba(0,0,0,.18);background:linear-gradient(180deg,#c9ced2,#8b9399)}
.card h3{font-family:"Nunito",sans-serif;font-weight:700;color:var(--teal-head);font-size:27px}
.card .role{color:var(--teal-head);font-weight:700;font-size:15px;margin-top:2px}
.card p{font-size:13.5px;line-height:17px;color:var(--ink);margin-top:14px}
.card .links{color:var(--teal-head);margin-top:18px}

/* discovery */
.steps{left:100px;top:2995px;width:1000px;height:320px;display:flex}
.step{position:relative;width:250px;height:320px;color:#fff;text-align:center;padding-top:40px}
.step:nth-child(1){background:var(--teal-deep)}
.step:nth-child(2){background:var(--teal)}
.step:nth-child(3){background:var(--teal-dark)}
.step:nth-child(4){background:#52b9cc}
.step .arrow{position:absolute;right:-14px;top:150px;width:0;height:0;border-top:14px solid transparent;border-bottom:14px solid transparent;z-index:2}
.step:nth-child(1) .arrow{border-left:14px solid var(--teal-deep)}
.step:nth-child(2) .arrow{border-left:14px solid var(--teal)}
.step:nth-child(3) .arrow{border-left:14px solid var(--teal-dark)}
.step h4{font-family:"Nunito",sans-serif;font-size:16px;font-weight:700;margin-top:14px}
.step p{font-size:12.5px;line-height:16px;margin-top:10px}

/* plan elements */
.plan{left:100px;top:3470px;width:1000px;font-size:14.5px;line-height:21px}
.plan li{margin-bottom:7px}
.plan b{color:var(--teal-head);font-weight:700}

/* contact */
.foot-wave{left:0;top:4180px}
.contact{left:100px;top:3870px;width:1000px;height:470px;background:#fff;box-shadow:0 4px 22px rgba(40,80,95,.16);display:flex}
.form{width:520px;padding:40px 34px}
.form h3,.details h3{font-family:"Nunito",sans-serif;font-weight:600;font-size:32px;letter-spacing:.5px}
.form h3{color:var(--teal-head)}
.grid{display:grid;grid-template-columns:1fr 1fr;gap:16px 20px;margin-top:30px}
.field{height:38px;border:1px solid var(--line);font-size:11px;color:#8a9196;padding:11px 10px;letter-spacing:.5px}
.field.msg{grid-column:1/3;height:130px}
.send{margin-top:16px;height:42px;background:var(--teal);color:#fff;font-size:12px;font-weight:700;letter-spacing:1px;display:flex;align-items:center;justify-content:center}
.details{width:480px;background:var(--teal);color:#fff;padding:40px 34px;border:4px solid #fff;border-left:0}
.drow{display:flex;align-items:center;gap:16px;margin-top:30px;font-size:14.5px;line-height:20px}
.drow.big{font-size:22px}
.social{border-top:1px solid rgba(255,255,255,.5);margin-top:34px;padding-top:22px;display:flex;gap:26px;font-size:14px}
.social span{display:flex;align-items:center;gap:8px}
.social i{width:22px;height:22px;border-radius:50%;background:#fff;display:inline-block}
.brand-foot{left:0;top:4385px;width:1200px;text-align:center;color:#fff;font-family:"Nunito",sans-serif;font-weight:900;font-size:48px}
.copy{left:0;top:4500px;width:1200px;height:85px;border-top:1px solid rgba(255,255,255,.55);color:#fff;font-size:12px;text-align:center;padding-top:30px;letter-spacing:.4px}
</style>
</head>
<body>
<div class="page">

  <header class="abs hero">
    <nav class="nav">
      <a href="#">Home</a><a href="#">Our Solutions</a><a href="#">Meet The Team</a><a href="#">K7 Plan Elements</a><a href="#">Contact Us</a>
    </nav>
    <h1 class="hero-title">The K7<br>Momentum<br>Collective™</h1>
    <div class="hero-tag">Accelerating your innovative IP to market!</div>
    <div class="btn-contact">Contact Us
      <svg width="16" height="22" viewBox="0 0 16 22"><path d="M8 2v16M3 13l5 5 5-5M2 21h12" fill="none" stroke="#fff" stroke-width="1.4"/></svg>
    </div>
    <div class="hero-art" role="img" aria-label="Illustration of business people pushing and climbing a set of large interlocking gears labelled resources, strategy, planning and control"></div>
    <svg class="hero-wave" width="1200" height="180" viewBox="0 0 1200 180"><path d="M0 110 C160 40 320 50 470 95 C640 145 800 160 960 110 C1060 80 1140 70 1200 80 L1200 180 L0 180 Z" fill="#fff"/></svg>
  </header>

  <div class="abs intro-art" role="img" aria-label="Photo of white jigsaw pieces with one red piece reading K7 the missing piece"></div>
  <section class="abs intro-text">
    <h2 class="h2">Introduction</h2>
    <div class="rule" style="margin-top:6px"></div>
    <p>The K7 Momentum Collective (K7) rapidly brings innovative and transformational IP to market by assisting with all elements of a company's development.</p>
    <p><em>We Are...</em>experienced in strategic business planning and execution, and operational excellence.</p>
    <p><em>We Have...</em>100 years of collective experiences and vast network of people, partners, and processes.</p>
    <p><em>We Can...</em>serve as the initial executive team to ensure strategic alignment with a focus on marketplace.</p>
    <p><em>We Will...</em>remove the uncertainty and confusion common in the initial stages of a company's formation.</p>
  </section>

  <svg class="abs band" width="1200" height="720" viewBox="0 0 1200 720"><path d="M0 110 C180 60 380 120 600 70 C820 20 1000 0 1200 40 L1200 560 C1060 660 880 640 700 600 C520 560 300 560 150 640 C90 670 40 690 0 700 Z" fill="#cdeff3"/><path d="M0 110 C180 60 380 120 600 70 C820 20 1000 0 1200 40 L1200 90 C1000 60 820 90 620 130 C400 170 200 120 0 160 Z" fill="#e4f7f9"/></svg>
  <section class="abs problem">
    <h2 class="h2">The Problem &gt; The Solution</h2>
    <div class="rule" style="margin-top:6px"></div>
    <p>K7 was started to solve significant problems associated with rapidly bringing innovative and transformational IP to market.</p>
    <div class="lead">These costly problems include:</div>
    <ul class="ticks">
      <li>Incomplete strategic planning,</li>
      <li>Difficulty finding leadership,</li>
      <li>Not able to differentiate a product or service from others that are already available, and Ignoring the needs of customer.</li>
      <li>(Capital shortages, poor locations, and scaling too soon can also cause a start-up to have problems.)</li>
    </ul>
    <p>The K7 Plan is unique to your organizational needs and secures the right people, partners, and processes to ensure an efficient start-up with strategic growth, and access to funding sources to help scale the business.</p>
  </section>
  <div class="abs problem-art" role="img" aria-label="Illustration of a team assembling blue puzzle platforms under a glowing light bulb idea"></div>

  <h2 class="abs h2 center" style="top:2170px">Meet The Team</h2>
  <div class="abs rule" style="left:572px;top:2225px"></div>
  <section class="abs team">
    <article class="card">
      <div class="avatar" role="img" aria-label="Portrait photo of Dana Whitlow"></div>
      <h3>Dana Whitlow</h3><div class="role">Partner</div>
      <p>Marketing, Commercial Development, Product Development, Growth Strategy</p>
      <p>30+ years of marketing, sales, product development, and operations executive leader in the life science and diagnostic industries.</p>
      <p class="links">(555) 014-2231<br>dana@k7mc.com<br>https://profiles.k7mc.com/<br>dana-whitlow-28c41a/</p>
    </article>
    <article class="card">
      <div class="avatar" role="img" aria-label="Portrait photo of Mira Castellan"></div>
      <h3>Mira Castellan</h3><div class="role">Partner</div>
      <p>Regulatory, Quality, Product Development, Operations</p>
      <p>30+ years working in diagnostic and medical device area with focus on creative solutions to bring product to market.</p>
      <p class="links">(555) 018-7740<br>mira@k7mc.com<br>https://profiles.k7mc.com/<br>mira-castellan/</p>
    </article>
    <article class="card">
      <div class="avatar" role="img" aria-label="Portrait photo of Owen Pryce"></div>
      <h3>Owen Pryce</h3><div class="role">Partner</div>
      <p>Board Development, Funding, Back-office Set-up, Operations</p>
      <p>30+ years accomplished CEO and well-rounded executive with more than 25 years of experience in medical devices, research tools and diagnostics.</p>
      <p class="links">(555) 012-5596<br>owen@k7mc.com<br>https://profiles.k7mc.com/<br>owen-pryce-77310b/</p>
    </article>
  </section>

  <h2 class="abs h2 center" style="top:2868px">Discovery to Market</h2>
  <div class="abs rule" style="left:572px;top:2923px"></div>
  <section class="abs steps">
    <div class="step"><span class="arrow"></span>
      <svg width="64" height="64" viewBox="0 0 64 64" fill="none" stroke="#fff" stroke-width="3"><circle cx="32" cy="32" r="12"/><circle cx="32" cy="10" r="5"/><circle cx="32" cy="54" r="5"/><circle cx="11" cy="22" r="5"/><circle cx="53" cy="22" r="5"/><circle cx="11" cy="43" r="5"/><circle cx="53" cy="43" r="5"/></svg>
      <h4>Discovery</h4>
    </div>
    <div class="step"><span class="arrow"></span>
      <svg width="64" height="64" viewBox="0 0 64 64" fill="none" stroke="#fff" stroke-width="3"><path d="M32 14a14 14 0 0 0-8 25v7h16v-7a14 14 0 0 0-8-25z"/><path d="M26 52h12M32 2v6M10 26H4M60 26h-6M15 10l4 4M49 10l-4 4"/></svg>
      <h4>Innovative IP</h4>
      <p>Inventor Disclosure<br>Provisional Patent<br>Licensing agreement</p>
    </div>
    <div class="step"><span class="arrow"></span>
      <svg width="64" height="64" viewBox="0 0 64 64" fill="none" stroke="#fff" stroke-width="3"><rect x="6" y="8" width="52" height="36"/><path d="M22 44l-8 14M42 44l8 14M32 44v10M14 34l10-10 8 6 14-14"/></svg>
      <h4>Strategic Business Plan</h4>
      <p>Invention Assessment<br>Voice of Customer<br>Product Definition<br><br>Business Model/Plan<br>Pitch Deck</p>
    </div>
    <div class="step">
      <svg width="64" height="64" viewBox="0 0 64 64" fill="none" stroke="#fff" stroke-width="3"><rect x="12" y="8" width="38" height="50" rx="3"/><rect x="24" y="4" width="14" height="8"/><path d="M20 26l4 4 7-7M20 42l4 4 7-7M36 28h8M36 44h8"/></svg>
      <h4>Company Formation</h4>
      <p>Experienced management<br>How to build out the initial team<br>Product definition<br>Business model<br>Org structure &amp; planning<br>Cash planning<br>Fund raising</p>
    </div>
  </section>

  <h2 class="abs h2 center" style="top:3375px">K7 Plan Elements</h2>
  <div class="abs rule" style="left:572px;top:3430px"></div>
  <ul class="abs plan ticks">
    <li><b>Executive Summary:</b> Articulates a brief snapshot of the business model/plan, including name, location, products or services, mission statement, and organizational values/ cultural beliefs.</li>
    <li><b>Company Description:</b> Describes a high-level view of the business nature, customer need being met, history, legality, short term, and long-term goals.</li>
    <li><b>Products/Services:</b> Provides a description of the product/services, its competitive advantages, customer benefits, reimbursement, estimated supplier costs, the net revenue from the sale of the product or service and after sale support.</li>
    <li><b>Market Analysis:</b> Displays research and plan to reach the target demographic as well as the size, direction, and competitors in the overall industry.</li>
    <li><b>Operations/Strategy:</b> Explains how the company will function given the sales and marketing strategy, and the plan of operations from acquisition of suppliers to delivery, including regulatory and quality plan.</li>
    <li><b>Financials:</b> Details estimates of all the important, financial documents, including balance sheet, cash flow, statement, capital, expenditure, budget, and income statement.</li>
    <li><b>Organization &amp; Management Team:</b> Shows the company structure as well as identifying divisions and key management personnel.</li>
  </ul>

  <svg class="abs foot-wave" width="1200" height="405" viewBox="0 0 1200 405"><path d="M0 90 C200 40 380 60 560 100 C760 140 960 120 1200 60 L1200 405 L0 405 Z" fill="#4bb4c8"/></svg>

  <section class="abs contact">
    <div class="form">
      <h3>CONTACT US</h3>
      <div class="grid">
        <div class="field">FIRST NAME*</div><div class="field">LAST NAME*</div>
        <div class="field">E-MAIL*</div><div class="field">PHONE*</div>
        <div class="field msg">MESSAGE</div>
      </div>
      <div class="send">SEND NOW</div>
    </div>
    <div class="details">
      <h3>CONTACT DETAILS</h3>
      <div class="drow"><svg width="26" height="32" viewBox="0 0 26 32"><path d="M13 1a12 12 0 0 0-12 12c0 9 12 18 12 18s12-9 12-18A12 12 0 0 0 13 1z" fill="#fff"/><circle cx="13" cy="13" r="5" fill="#4bb4c8"/></svg><span>4800 Harborview Lane Suite 210,<br>Brookmere, ST 40812</span></div>
      <div class="drow big"><svg width="30" height="30" viewBox="0 0 30 30"><circle cx="15" cy="15" r="15" fill="#fff"/><path d="M10 8l3 0 1 4-2 1.5a9 9 0 0 0 4.5 4.5L18 16l4 1v3c-7 1-13-5-12-12z" fill="#4bb4c8"/></svg><span>(555) 010-4477</span></div>
      <div class="drow"><svg width="30" height="30" viewBox="0 0 30 30"><circle cx="15" cy="15" r="15" fill="#fff"/><rect x="8" y="10" width="14" height="10" fill="none" stroke="#4bb4c8" stroke-width="1.6"/><path d="M8 10l7 6 7-6" fill="none" stroke="#4bb4c8" stroke-width="1.6"/></svg><span>hello@k7mc.com</span></div>
      <div class="social"><span><i></i>Chatterbook</span><span><i></i>Birdline</span><span><i></i>Linkwork</span></div>
    </div>
  </section>

  <div class="abs brand-foot">The K7 Momentum Collective™</div>
  <div class="abs copy">© 2023 THE K7 MOMENTUM COLLECTIVE - ALL RIGHTS RESERVED</div>
</div>
</body>
</html>
```